Business card design needed

A earthmoving company, in the background would be good if there could be a picture of a (scraper), we have a business card already with lumo stack you may be able to see that?

Industry/Entity Type

Business

Contact Information for Business Card

Company name: Brindle Earthmoving

Corwin Brindle
514 Tarrabin-Keswell Rd
Mount Kelwyn
4815
0491 736 052
corwin_brindle@mailbrook.net

on the rear of the card
Equipment Hire and Contract

All Earthmoving, Mining and Civil Contruction

```html
<!DOCTYPE html>
<html lang="en">
<head>
<meta charset="utf-8">
<title>Brindle Earthmoving – Business Card</title>
<link rel="stylesheet" href="https://fonts.googleapis.com/css2?family=Arimo:wght@400;700&display=swap">
<style>
  :root {
    --canvas: #ffffff;
    --yellow: #eeb021;
    --black: #000000;
    --grey: #c9c9c9;
    --sky-top: #3f8fd0;
    --sky-light: #bcdcf2;
    --dirt: #b88a5c;
    --dirt-dark: #8e6644;
    --ink: #111111;
  }
  html, body {
    margin: 0;
    padding: 0;
    width: 1200px;
    height: 1200px;
    overflow: hidden;
    background: var(--canvas);
    font-family: "Arimo", Arial, sans-serif;
  }
  .canvas {
    position: relative;
    width: 1200px;
    height: 1200px;
  }
  .card {
    position: absolute;
    background: var(--yellow);
    overflow: hidden;
  }
  .card--front { left: 308px; top: 115px; width: 647px; height: 365px; }
  .card--back  { left: 309px; top: 599px; width: 650px; height: 368px; }

  .band {
    position: absolute;
    left: 0;
    width: 100%;
    background: var(--black);
  }
  .card--front .band { top: 48px; height: 112px; }
  .card--back .band  { top: 49px; height: 111px; }

  .pointer {
    position: absolute;
    width: 0;
    height: 0;
    border-left: 10px solid transparent;
    border-right: 10px solid transparent;
    border-top: 16px solid var(--black);
  }
  .card--front .pointer { left: 265px; top: 160px; }
  .card--back .pointer  { left: 61px; top: 160px; }

  .photo-sky {
    position: absolute;
    left: 0; top: 0;
    width: 251px; height: 48px;
    background: linear-gradient(180deg, var(--sky-top), var(--sky-light));
  }
  .photo-site {
    position: absolute;
    left: 0; top: 160px;
    width: 251px; height: 205px;
    background: linear-gradient(180deg, var(--sky-top) 0%, var(--sky-light) 35%, var(--dirt) 60%, var(--dirt-dark) 100%);
  }

  .brand-mark {
    position: absolute;
    width: 30px;
    height: 30px;
    background: var(--grey);
  }
  .card--front .brand-mark { left: 60px; top: 89px; }

  .brand-name {
    position: absolute;
    margin: 0;
    font-weight: 700;
    color: var(--grey);
    text-transform: uppercase;
    letter-spacing: 1px;
    line-height: 1.05;
  }
  .card--front .brand-name {
    left: 305px; top: 68px;
    width: 290px;
    font-size: 34px;
    text-align: center;
  }
  .card--back .brand-name {
    left: 58px; top: 74px;
    font-size: 30px;
    width: 250px;
  }

  .contact {
    position: absolute;
    left: 272px;
    top: 186px;
    margin: 0;
    font-size: 18.5px;
    line-height: 25px;
    color: var(--ink);
    font-style: normal;
  }
  .contact .email {
    display: block;
    margin-top: 24px;
  }

  .services {
    position: absolute;
    left: 63px;
    top: 218px;
    margin: 0;
    padding: 0;
    list-style: none;
    font-size: 29px;
    line-height: 37.5px;
    color: var(--ink);
  }
  .services li {
    position: relative;
    padding-left: 16px;
  }
  .services li::before {
    content: "";
    position: absolute;
    left: 0;
    top: 15px;
    width: 9px;
    height: 9px;
    border-radius: 50%;
    background: var(--ink);
  }
</style>
</head>
<body>
<main class="canvas">
  <section class="card card--front" aria-label="Business card front">
    <div class="photo-sky" role="img" aria-label="Blue sky with clouds above the work site"></div>
    <div class="band"></div>
    <div class="pointer"></div>
    <div class="photo-site" role="img" aria-label="Photo of a yellow scraper on a dirt earthmoving site"></div>
    <div class="brand-mark"></div>
    <h1 class="brand-name">Brindle Earthmoving</h1>
    <address class="contact">
      Corwin Brindle<br>
      514 Tarrabin-Keswell Rd<br>
      Mount Kelwyn<br>
      4815 0491 736 052
      <span class="email">corwin_brindle@mailbrook.net</span>
    </address>
  </section>

  <section class="card card--back" aria-label="Business card back">
    <div class="band"></div>
    <div class="pointer"></div>
    <p class="brand-name">Brindle Earthmoving</p>
    <ul class="services">
      <li>Equipment Hire and Contract</li>
      <li>All Earthmoving</li>
      <li>Mining and Civil Contruction</li>
    </ul>
  </section>
</main>
</body>
</html>
```